Kravin House Music DJ Chatterly Banner

Hi there,
This is for a house music dj Chatterly site. Looking for the top banner to replace my page. You can check put Kravin on Chatterly to see the banner.
The name Kravin is pronounced like Fossil. use Dinosaurs a lot in my music. The whole idea is because I an older DJ. A fossil. I need a cool banner I can also use on Chatterly and Blinkpost.

https://www.chatterlyhub.com/Kravin

Target Market(s)

Target market is people who enjoy house music, EDM, dance music, etc.

Industry/Entity Type

House

Font styles to use
Sans Serif

Requirements
Must have
• The banner must be modern and cool looking appealing to EDM music lovers
• Must be reflective of my "fossil" theme but use my dj name Kravin
Nice to have
• Dinosaur feel but not cartoony.
• Steel or fossil look
Should not have
• DO NOT say DJ KRAVIN. Only Kravin
• Do not use the uploads in the design. Looking for a new concept completely

```html
<!DOCTYPE html>
<html lang="en">
<head>
<meta charset="utf-8">
<title>Kravin – Banner</title>
<link rel="stylesheet" href="https://fonts.googleapis.com/css2?family=Audiowide&display=swap">
<style>
  :root {
    --skin-dark: #2a1a22;
    --skin-mid: #6e4d5a;
    --skin-light: #9c7f86;
    --laser-violet: #9a4cf0;
    --laser-magenta: #e04ac8;
    --laser-blue: #4a78ff;
    --laser-red: #ff5a6a;
    --laser-cyan: #7fd8ff;
    --bone-light: #cbbcd6;
    --bone-mid: #7a6688;
    --bone-shadow: #140e16;
    --patch: #22102e;
    --patch-edge: #3e1d58;
    --steel-top: #f6f2fc;
    --steel-mid: #c2b4d2;
    --steel-low: #6a5a84;
  }
  html, body {
    margin: 0;
    padding: 0;
    overflow: hidden;
    background: #111;
  }
  .banner {
    position: relative;
    width: 1200px;
    height: 443px;
    overflow: hidden;
  }
  .skin-texture {
    position: absolute;
    inset: 0;
    background:
      radial-gradient(ellipse 38% 55% at 72% 42%, rgba(154,76,240,.6), transparent 72%),
      radial-gradient(ellipse 26% 40% at 52% 30%, rgba(224,74,200,.35), transparent 72%),
      radial-gradient(ellipse 30% 40% at 88% 82%, rgba(74,120,255,.3), transparent 72%),
      linear-gradient(160deg, var(--skin-light) 0%, var(--skin-mid) 40%, #4a3038 75%, var(--skin-dark) 100%);
  }
  .lasers {
    position: absolute;
    inset: 0;
    mix-blend-mode: screen;
  }
  .skeleton {
    position: absolute;
    left: 0;
    top: 0;
    width: 520px;
    height: 443px;
    background:
      radial-gradient(ellipse 42% 34% at 58% 28%, var(--bone-light), rgba(122,102,136,.6) 60%, transparent 100%),
      radial-gradient(ellipse 26% 40% at 44% 72%, rgba(180,166,196,.7), transparent 80%),
      radial-gradient(circle 30px at 26% 55%, rgba(255,255,255,.95), rgba(255,255,255,0) 100%),
      linear-gradient(90deg, var(--bone-shadow) 0%, #3a2c42 30%, var(--bone-mid) 62%, rgba(122,102,136,0) 100%);
  }
  .title-art {
    position: absolute;
    left: 0;
    top: 0;
  }
  .title {
    font-family: "Audiowide", sans-serif;
    font-weight: 400;
    font-size: 118px;
  }
</style>
</head>
<body>
  <div class="banner">
    <div class="skin-texture" role="img" aria-label="Scaled reptile skin texture with violet and magenta glow"></div>
    <svg class="lasers" width="1200" height="443" viewBox="0 0 1200 443" aria-hidden="true">
      <g stroke-width="1.6" opacity=".75" fill="none">
        <line x1="560" y1="0" x2="1200" y2="300" stroke="var(--laser-blue)"/>
        <line x1="620" y1="0" x2="900" y2="443" stroke="var(--laser-magenta)"/>
        <line x1="700" y1="0" x2="520" y2="443" stroke="var(--laser-violet)"/>
        <line x1="820" y1="0" x2="1200" y2="420" stroke="var(--laser-cyan)"/>
        <line x1="900" y1="0" x2="640" y2="443" stroke="var(--laser-red)"/>
        <line x1="1000" y1="0" x2="760" y2="443" stroke="var(--laser-blue)"/>
        <line x1="1200" y1="60" x2="480" y2="380" stroke="var(--laser-magenta)"/>
        <line x1="1200" y1="140" x2="600" y2="0" stroke="var(--laser-violet)"/>
        <line x1="460" y1="120" x2="1200" y2="220" stroke="var(--laser-cyan)"/>
        <line x1="480" y1="443" x2="1100" y2="0" stroke="var(--laser-red)"/>
        <line x1="560" y1="443" x2="1200" y2="110" stroke="var(--laser-blue)"/>
        <line x1="760" y1="0" x2="1080" y2="443" stroke="var(--laser-red)"/>
        <line x1="1060" y1="0" x2="980" y2="443" stroke="var(--laser-magenta)"/>
        <line x1="1160" y1="0" x2="860" y2="443" stroke="var(--laser-blue)"/>
        <line x1="500" y1="250" x2="1200" y2="360" stroke="var(--laser-violet)"/>
        <line x1="420" y1="40" x2="1200" y2="20" stroke="var(--laser-magenta)"/>
        <line x1="640" y1="443" x2="1200" y2="260" stroke="var(--laser-red)"/>
        <line x1="940" y1="443" x2="1200" y2="180" stroke="var(--laser-cyan)"/>
        <line x1="880" y1="0" x2="1200" y2="40" stroke="var(--laser-blue)"/>
        <line x1="440" y1="180" x2="760" y2="0" stroke="var(--laser-cyan)"/>
      </g>
    </svg>
    <div class="skeleton" role="img" aria-label="Tyrannosaurus fossil skeleton with open jaws, lit in pale violet, with a bright lens flare"></div>
    <svg class="title-art" width="1200" height="443" viewBox="0 0 1200 443">
      <defs>
        <linearGradient id="steel" x1="0" y1="0" x2="0" y2="1">
          <stop offset="0" stop-color="var(--steel-top)"/>
          <stop offset=".55" stop-color="var(--steel-mid)"/>
          <stop offset="1" stop-color="var(--steel-low)"/>
        </linearGradient>
        <filter id="drop" x="-5%" y="-20%" width="110%" height="140%">
          <feDropShadow dx="3" dy="5" stdDeviation="2" flood-color="#0a0410" flood-opacity=".85"/>
        </filter>
      </defs>
      <polygon fill="var(--patch)" stroke="var(--patch-edge)" stroke-width="3" opacity=".92"
        points="446,196 520,178 610,190 700,170 820,186 930,168 1040,182 1150,166 1185,178 1175,300 1110,290 1010,306 900,292 780,312 660,296 560,304 470,292 440,250"/>
      <text class="title" x="468" y="275" textLength="690" lengthAdjust="spacingAndGlyphs"
        fill="url(#steel)" stroke="#3a2a4e" stroke-width="1.5" filter="url(#drop)">KRAVIN</text>
    </svg>
  </div>
</body>
</html>
```